Create a new business card

I’m looking to update my business card to make it match the rest of my brand. I will include my current website as well as what my vehicle designs look like, etc..
What my business currently services
Weekly maintenance pool openings / closings
Equipment repair, including pumps, heaters, salt systems, filters, etc.
We install automatic covers and maintain them as well as provide preventative maintenance

I would like to include my name.
Darren Holcott.
My title
Owner
My email
Darren@tidewellnx.com
4015867120
Www.tidewellnx.com

```html
<!DOCTYPE html>
<html lang="en">
<head>
<meta charset="utf-8">
<title>Tidewell Pool Care – Business Card</title>
<link rel="stylesheet" href="https://fonts.googleapis.com/css2?family=Roboto:wght@400;500;700&display=swap">
<style>
  :root {
    --bg: #bdbdbd;
    --navy: #27326f;
    --navy-light: #34438a;
    --sky: #2ab0e6;
    --sky-deep: #1c74c9;
    --blue-dark: #17398f;
    --white: #ffffff;
  }
  * { box-sizing: border-box; margin: 0; padding: 0; }
  html, body { width: 1200px; height: 876px; overflow: hidden; }
  body {
    background: var(--bg);
    font-family: "Roboto", Arial, sans-serif;
    position: relative;
  }
  .card {
    position: absolute;
    top: 283px;
    width: 540px;
    height: 310px;
    border-radius: 22px;
    overflow: hidden;
  }
  .card--front { left: 40px; background: linear-gradient(135deg, var(--navy) 0%, var(--navy-light) 55%, var(--navy) 100%); }
  .card--back {
    left: 620px;
    background: radial-gradient(circle at 45% 45%, var(--sky) 0%, var(--sky-deep) 60%, var(--blue-dark) 100%);
  }
  .card__shape { position: absolute; inset: 0; width: 100%; height: 100%; }

  .owner { position: absolute; left: 120px; top: 42px; }
  .owner__name { color: var(--sky); font-size: 21px; font-weight: 500; text-transform: uppercase; letter-spacing: 0.3px; }
  .owner__title { color: var(--white); font-size: 14px; margin-top: 2px; }

  .contact { position: absolute; left: 46px; top: 132px; list-style: none; }
  .contact__item { display: flex; align-items: center; gap: 10px; color: var(--white); font-size: 16px; margin-bottom: 9px; }
  .contact__icon { width: 14px; height: 14px; flex: none; }

  .brand {
    position: absolute;
    color: var(--navy);
    font-weight: 700;
    text-align: center;
    line-height: 1.1;
  }
  .card--front .brand { left: 310px; top: 165px; width: 200px; font-size: 26px; }
  .card--back .brand { left: 170px; top: 118px; width: 200px; font-size: 28px; }
  .brand__url { display: block; font-size: 11px; margin-top: 8px; letter-spacing: 0.5px; }
</style>
</head>
<body>
  <section class="card card--front" aria-label="Card front">
    <svg class="card__shape" viewBox="0 0 540 310" aria-hidden="true">
      <circle cx="420" cy="250" r="178" fill="none" stroke="var(--sky)" stroke-width="5"/>
      <circle cx="424" cy="256" r="172" fill="var(--white)"/>
    </svg>
    <div class="owner">
      <p class="owner__name">Darren Holcott</p>
      <p class="owner__title">Owner</p>
    </div>
    <ul class="contact">
      <li class="contact__item">
        <svg class="contact__icon" viewBox="0 0 14 14"><circle cx="7" cy="7" r="7" fill="var(--sky)"/><path d="M4.5 3.5l1.5 1.6-.8 1a5 5 0 0 0 2.7 2.7l1-.8 1.6 1.5-.9 1A6.5 6.5 0 0 1 3.5 4.4z" fill="var(--navy)"/></svg>
        4015867120
      </li>
      <li class="contact__item">
        <svg class="contact__icon" viewBox="0 0 14 14"><rect x="1" y="3" width="12" height="8" rx="1" fill="var(--sky)"/><path d="M1 3.5l6 4 6-4" fill="none" stroke="var(--navy)" stroke-width="1.2"/></svg>
        Darren@tidewellnx.com
      </li>
      <li class="contact__item">
        <svg class="contact__icon" viewBox="0 0 14 14"><circle cx="7" cy="7" r="7" fill="var(--sky)"/><path d="M2 7h10M7 1.5c-2.5 3-2.5 8 0 11M7 1.5c2.5 3 2.5 8 0 11" fill="none" stroke="var(--navy)" stroke-width="1"/></svg>
        www.tidewellnx.com
      </li>
    </ul>
    <p class="brand">Tidewell Pool Care<span class="brand__url">WWW.TIDEWELLNX.COM</span></p>
  </section>

  <section class="card card--back" aria-label="Card back">
    <svg class="card__shape" viewBox="0 0 540 310">
      <circle cx="270" cy="150" r="118" fill="var(--white)" role="img" aria-label="White water splash behind the company name"/>
    </svg>
    <p class="brand">Tidewell Pool Care<span class="brand__url">WWW.TIDEWELLNX.COM</span></p>
  </section>
</body>
</html>
```